ROOFING DISTRIBUTOR LOCATION NEEDS BUSINESS. POST CARD DESIGN FOR MAILOUT

Need a post card with general information about the company.

Over-sized Post Card

* We are a wholesale roofing distributor

* Taglines: "A Tradition Since 1905" & "Building Relationships, Building Trust - a Tradition Since 1905"

* Products offered:
Shingles (VORLEX, BrightFrame, Pallister Ridge, HUV)
Steel Roofing (Iron Crest, Voltan, Zarle) - EPDM & TPO (Brennick) Aluminum Soffit, Fascia, Siding (QT Cladwise, Norbert Quill)
Windows (Tall Pane, Stormvessel)

* Services Offered:
Prompt Response to inquiries
Safe & Efficient Job-site Delivery
Free Tapered Take-Off Serive
Training/Application Seminars
Friendly & Knowledgeable Customer Service
Timely Accurate Invoicing

Address:
7183 Kettering Rd. Madison, WI 53704

Phone:
(608) 555-0143

Fax:
(608) 555-0178

Email:
tbrandt@harborfinchsupply.example (Trevor Brandt, Branch Manager)

website: www.harborfinchsupply.example

Target Market(s)

roofing contractors

Industry/Entity Type

Business

Font styles to use
Sans Serif

Colors
0355a3

Requirements
Must have
• company logo and contact info
Nice to have
• vendor logos and taglines

```html
<!DOCTYPE html>
<html lang="en">
<head>
<meta charset="utf-8">
<title>Harbor Finch Supply Postcard</title>
<link href="https://fonts.googleapis.com/css2?family=Oswald:wght@500;700&family=Open+Sans:wght@400;600;700&display=swap" rel="stylesheet">
<style>
:root{
  --brand:#0355a3;
  --brand-dark:#023a73;
  --brand-deep:#012a55;
  --sky:#cfe3f5;
  --paper:#ffffff;
  --ink:#1d2a3a;
  --muted:#8a97a6;
  --stage:#e9ecef;
}
*{margin:0;padding:0;box-sizing:border-box}
html,body{width:853px;height:1200px;overflow:hidden;background:var(--stage)}
body{position:relative;font-family:"Open Sans",Arial,sans-serif;color:var(--ink)}
.card{position:absolute;left:20px;width:813px;height:560px;background:var(--paper);overflow:hidden;box-shadow:0 4px 14px rgba(0,0,0,.25)}
.card--front{top:20px}
.card--back{top:620px}
.abs{position:absolute}
.photo{position:absolute}

/* front */
.front-hero{left:330px;top:0;width:483px;height:560px;background:linear-gradient(160deg,#e9f2fb 0%,#a9c8e6 40%,#d88a3a 70%,#b9876a 100%)}
.front-panel{left:0;top:0;width:460px;height:560px}
.tagline{left:30px;top:26px;color:#fff;font-family:"Oswald",Arial,sans-serif;font-weight:500;font-size:19px;letter-spacing:.5px}
.headline{font-family:"Oswald",Arial,sans-serif;font-weight:700;color:#fff;text-transform:uppercase;letter-spacing:.5px}
.front-headline{left:28px;top:50px;font-size:40px}
.thumbs{left:32px;top:118px;display:flex;gap:14px}
.thumb{width:72px;height:72px;border-radius:50%;border:3px solid #fff;background:linear-gradient(160deg,#b8cfe3,#7d6a5a)}
.products{left:34px;top:215px;width:330px;list-style:none;color:#fff;font-size:12px;line-height:1.35}
.products li{position:relative;padding-left:12px;margin-bottom:5px}
.products li::before{content:"";position:absolute;left:0;top:6px;width:5px;height:5px;background:#fff;border-radius:50%}
.logo-box{left:60px;top:355px;width:210px;height:110px;background:#fff;border-radius:8px;display:flex;align-items:center;justify-content:center;gap:8px;padding:0 12px}
.logo-dot{width:16px;height:16px;border-radius:50%;background:var(--brand);flex:none}
.logo-name{font-family:"Oswald",Arial,sans-serif;font-weight:700;font-size:19px;color:var(--brand);letter-spacing:.5px}

/* back */
.back-band{left:0;top:0;width:813px;height:150px}
.back-headline{left:34px;top:26px;font-size:40px}
.services{left:40px;top:140px;width:440px;display:grid;grid-template-columns:1fr 1fr;gap:0 20px;list-style:none;font-size:12px;line-height:1.35;color:var(--ink)}
.services li{position:relative;padding-left:12px;margin-bottom:5px}
.services li::before{content:"";position:absolute;left:0;top:6px;width:5px;height:5px;background:var(--brand);border-radius:50%}
.back-lower{left:0;top:250px;width:480px;height:310px}
.cta{left:30px;top:320px;color:#fff}
.cta-label{font-family:"Oswald",Arial,sans-serif;font-weight:700;font-size:22px}
.cta-phone{font-family:"Oswald",Arial,sans-serif;font-weight:700;font-size:24px}
.truck{left:215px;top:292px;width:240px;height:120px;background:linear-gradient(180deg,#dfe9f3 0%,#f4f6f8 55%,#6e7780 100%);border-radius:4px}
.contact{left:30px;top:430px;list-style:none;color:#fff;font-size:11.5px;line-height:1.65}
.contact li{display:flex;align-items:center;gap:6px}
.contact svg{flex:none}
.divider{left:500px;top:170px;width:1px;height:360px;background:#c9d2dc}
.stamp{left:700px;top:170px;width:72px;height:84px;border:1.5px solid #9aa6b2}
.figure{left:560px;top:200px;width:110px;height:170px;background:radial-gradient(ellipse at center,rgba(140,160,180,.28),rgba(140,160,180,0) 70%)}
.address-lines{left:560px;top:410px;width:215px}
.address-lines span{display:block;height:1px;background:#9aa6b2;margin-bottom:26px}
</style>
</head>
<body>

<section class="card card--front" aria-label="Postcard front">
  <div class="photo front-hero" role="img" aria-label="Roofer in a yellow hard hat and orange shirt working on a roof under a blue sky"></div>
  <svg class="abs front-panel" viewBox="0 0 460 560" aria-hidden="true">
    <path d="M0 0H440C380 150 380 420 330 560H0Z" fill="#0355a3"/>
    <path d="M440 0C380 150 380 420 330 560H318C368 420 370 150 428 0Z" fill="#ffffff"/>
    <path d="M0 0H440C430 30 422 60 415 96H0Z" fill="#023a73"/>
    <path d="M0 500C140 470 260 500 340 470L330 560H0Z" fill="#012a55"/>
  </svg>
  <p class="abs tagline">BUILDING RELATIONSHIPS, BUILDING TRUST</p>
  <h1 class="abs headline front-headline">A Tradition Since 1905</h1>
  <div class="abs thumbs">
    <div class="thumb" role="img" aria-label="Shingled roof photo"></div>
    <div class="thumb" role="img" aria-label="Steel roofing photo"></div>
    <div class="thumb" role="img" aria-label="House siding and windows photo"></div>
  </div>
  <ul class="abs products">
    <li>Shingles (VORLEX, BrightFrame, Pallister Ridge, HUV)</li>
    <li>Steel Roofing (Iron Crest, Voltan, Zarle) - EPDM &amp; TPO (Brennick) Aluminum Soffit</li>
    <li>Fascia, Siding (QT Cladwise, Norbert Quill)</li>
    <li>Windows (Tall Pane, Stormvessel)</li>
  </ul>
  <div class="abs logo-box">
    <span class="logo-dot"></span>
    <span class="logo-name">HARBOR FINCH SUPPLY</span>
  </div>
</section>

<section class="card card--back" aria-label="Postcard back">
  <svg class="abs back-band" viewBox="0 0 813 150" aria-hidden="true">
    <path d="M0 0H813V80C600 70 560 120 440 110H0Z" fill="#cfe3f5"/>
    <path d="M0 0H520C500 40 480 80 440 110H0Z" fill="#0355a3"/>
    <path d="M520 0H540C520 50 490 95 440 122V110C480 80 500 40 520 0Z" fill="#ffffff"/>
  </svg>
  <h2 class="abs headline back-headline">A Tradition Since 1905</h2>
  <ul class="abs services">
    <li>Prompt Response to Inquiries</li>
    <li>Friendly &amp; Knowledgeable Customer Service</li>
    <li>Safe &amp; Efficient Job-site Delivery</li>
    <li>Timely Accurate Invoicing</li>
    <li>Free Tapered Take-Off Service</li>
    <li></li>
    <li>Training/Application Seminars</li>
  </ul>
  <svg class="abs back-lower" viewBox="0 0 480 310" aria-hidden="true">
    <path d="M0 40C160 0 330 20 480 30V310H0Z" fill="#0355a3"/>
    <path d="M0 250C150 220 300 250 480 225V310H0Z" fill="#012a55"/>
  </svg>
  <div class="abs cta">
    <p class="cta-label">CALL US TODAY</p>
    <p class="cta-phone">(608) 555-0143</p>
  </div>
  <div class="photo truck" role="img" aria-label="Delivery truck with boom loader carrying roofing materials"></div>
  <ul class="abs contact">
    <li><svg width="10" height="10" viewBox="0 0 10 10"><path d="M2 1l2 2-1 1.5c.8 1.4 1.6 2.2 3 3L7.5 6l2 2-1.5 1.5C4.5 9 1 5.5.5 2.5Z" fill="#fff"/></svg>(608) 555-0178</li>
    <li><svg width="10" height="10" viewBox="0 0 10 10"><path d="M5 0a3.5 3.5 0 0 1 3.5 3.5C8.5 6 5 10 5 10S1.5 6 1.5 3.5A3.5 3.5 0 0 1 5 0Zm0 2a1.5 1.5 0 1 0 0 3 1.5 1.5 0 0 0 0-3Z" fill="#fff"/></svg>7183 Kettering Rd. Madison, WI 53704</li>
    <li><svg width="10" height="10" viewBox="0 0 10 10"><rect x=".5" y="2" width="9" height="6" fill="none" stroke="#fff"/><path d="M.5 2 5 5.5 9.5 2" fill="none" stroke="#fff"/></svg>tbrandt@harborfinchsupply.example</li>
    <li><svg width="10" height="10" viewBox="0 0 10 10"><circle cx="5" cy="5" r="4.3" fill="none" stroke="#fff"/><path d="M.7 5h8.6M5 .7c2 2.4 2 6.2 0 8.6M5 .7c-2 2.4-2 6.2 0 8.6" fill="none" stroke="#fff" stroke-width=".7"/></svg>www.harborfinchsupply.example</li>
  </ul>
  <div class="abs divider"></div>
  <div class="abs stamp"></div>
  <div class="abs figure" role="img" aria-label="Faint silhouette of a roofer"></div>
  <div class="abs address-lines"><span></span><span></span><span></span><span></span></div>
</section>

</body>
</html>
```